Birchwood Recovery Center Billboard (Addiction / Alcohol / Opioid )

visit www.birchwoodrecovery-example.com
We are an inpatient treatment center for opioid, alcohol and drug addiction. We are looking to get multiple 12'x25' billboards in our area. Our Phone number is 1-844-HEAL-NOW we are located in Pinecrest Falls
We pride ourselves on a comfortable medical detox and treat our patients as family.

Target Market(s)

Current Addicts, Addicts family or friends, Factory Workers and Shopvale shoppers

Industry/Entity Type

Health Care

Font styles to use
Sans Serif

Colors
0355a3
3176b5
ffffff

Requirements
Must have
• Logo and Phone number, and Birchwood Recovery
Nice to have
• Ideas?
1.) Addiction hurts more than yourself. (Pic of little girl?)
2.) Just how much are you willing to lose?
3.) Addiction does not define you, You are what you choose to become.
4.) Indiana's most comfortable Detox
5.) Detox in unmatched comfort.
6.) Background could be patient room with logo in upper right
7.) Looking to be able to read easily from road.
Should not have
• Hard to read lettering

```html
<!DOCTYPE html>
<html lang="en">
<head>
<meta charset="utf-8">
<title>Birchwood Recovery Billboard</title>
<link rel="stylesheet" href="https://fonts.googleapis.com/css2?family=Open+Sans:wght@600;700;800&family=Lato:wght@400;700&display=swap">
<style>
  :root {
    --navy: #0b2a63;
    --cyan: #00c3f3;
    --cyan-light: #5fdcfb;
    --board-bg: #e5e0de;
    --photo-warm: #c9ada0;
    --photo-soft: #ded6d2;
    --white: #ffffff;
    --page: #f2f2f2;
  }
  * { box-sizing: border-box; margin: 0; padding: 0; }
  html, body { width: 1000px; height: 1200px; overflow: hidden; background: var(--page); }
  .billboard {
    position: absolute; left: 40px; top: 378px;
    width: 920px; height: 443px;
    background: var(--board-bg);
    overflow: hidden;
    font-family: "Open Sans", Arial, sans-serif;
  }
  .hero-photo {
    position: absolute; left: 0; top: 0; width: 520px; height: 443px;
    background:
      radial-gradient(ellipse 60% 70% at 42% 55%, var(--photo-warm) 0%, rgba(201,173,160,0.6) 55%, rgba(229,224,222,0) 100%),
      linear-gradient(90deg, var(--photo-soft) 0%, var(--board-bg) 100%);
  }
  .headline-group { font-size: inherit; }
  .headline { position: absolute; line-height: 1; white-space: nowrap; font-weight: 800; letter-spacing: -0.5px; }
  .headline--addiction { left: 462px; top: 38px; font-size: 48px; color: var(--cyan); }
  .headline--hurts { left: 396px; top: 74px; font-size: 82px; color: var(--navy); letter-spacing: -2px; }
  .headline--more { left: 508px; top: 146px; font-size: 31px; color: var(--cyan); }
  .headline--yourself { left: 420px; top: 164px; font-size: 82px; color: var(--navy); letter-spacing: -2px; }
  .brand {
    position: absolute; left: 724px; top: 30px; width: 160px;
    text-align: center; color: var(--navy);
  }
  .brand-mark {
    width: 72px; height: 72px; border-radius: 50%;
    background: var(--cyan); margin: 0 auto 14px;
  }
  .brand-name { font-weight: 600; font-size: 18px; line-height: 1.15; letter-spacing: 1.5px; text-transform: uppercase; }
  .contact-dome {
    position: absolute; left: 457px; top: 240px;
    width: 454px; height: 454px; border-radius: 50%;
    background: linear-gradient(180deg, var(--cyan-light) 0%, var(--cyan) 18%, var(--cyan) 100%);
  }
  .contact {
    position: absolute; left: 457px; width: 454px; text-align: center; color: var(--white);
    line-height: 1; white-space: nowrap;
  }
  .contact-label { top: 268px; font-family: "Lato", Arial, sans-serif; font-size: 19px; }
  .contact-city { top: 292px; font-family: "Lato", Arial, sans-serif; font-weight: 700; font-size: 23px; }
  .contact-rule { position: absolute; left: 587px; top: 331px; width: 193px; height: 1.5px; background: var(--white); }
  .contact-phone { top: 344px; font-weight: 700; font-size: 40px; letter-spacing: -0.5px; }
  .contact-web { top: 393px; font-weight: 700; font-size: 20px; }
</style>
</head>
<body>
  <main class="billboard">
    <div class="hero-photo" role="img" aria-label="Photo of a sad little girl sitting with her arms wrapped around her knees"></div>

    <h1 class="headline-group">
      <span class="headline headline--addiction">Addiction</span>
      <span class="headline headline--hurts">hurts</span>
      <span class="headline headline--more">more than</span>
      <span class="headline headline--yourself">yourself.</span>
    </h1>

    <div class="brand">
      <div class="brand-mark"></div>
      <p class="brand-name">Birchwood<br>Recovery</p>
    </div>

    <div class="contact-dome"></div>
    <p class="contact contact-label">Located in</p>
    <p class="contact contact-city">Pinecrest Falls</p>
    <div class="contact-rule"></div>
    <p class="contact contact-phone">1-844-HEAL-NOW</p>
    <p class="contact contact-web">www.birchwoodrecovery-example.com</p>
  </main>
</body>
</html>
```